Design business card for Bright Harbour Coaching!

I am a personal development coach (like a life coach) and corporate trainer and need a professionally designed double sided business card.

It needs to contain the business logo (I'm happy for the designer to choose the layout of the logo as I am still working out the best option myself) and the following information:

Tamsin Varga
Personal Development Coach and Trainer

+61 (0)452 819 407 (written that way)
tamsin@bright-harbour.com

www.bright-harbour.com

```html
<!DOCTYPE html>
<html lang="en">
<head>
<meta charset="utf-8">
<title>Bright Harbour Coaching – Business Card</title>
<link rel="stylesheet" href="https://fonts.googleapis.com/css2?family=Cinzel:wght@400&family=Arimo:wght@400;700&display=swap">
<style>
  :root {
    --teal: #1b97a3;
    --teal-dark: #157f8a;
    --ink: #1e1e1e;
    --paper: #ffffff;
    --backdrop: #e9e6e1;
    --logo-grey: #5a5a5a;
  }
  * { box-sizing: border-box; margin: 0; padding: 0; }
  html, body { width: 1200px; height: 950px; overflow: hidden; background: var(--backdrop); }
  .canvas { position: relative; width: 1200px; height: 950px; }

  .card {
    position: absolute;
    width: 560px;
    height: 342px;
    border-radius: 3px;
    box-shadow: 0 6px 18px rgba(0,0,0,.18);
    overflow: hidden;
  }

  /* Back: teal */
  .card-back { left: 80px; top: 90px; background: var(--teal); color: #fff; }
  .card-back .brand {
    position: absolute; left: 0; right: 0; top: 120px;
    display: flex; align-items: center; justify-content: center; gap: 14px;
  }
  .brand-dot { width: 30px; height: 30px; border-radius: 50%; background: #fff; flex: none; }
  .brand-name {
    font-family: "Cinzel", Georgia, serif; font-weight: 400;
    font-size: 26px; letter-spacing: .5px; white-space: nowrap;
  }
  .card-back .web {
    position: absolute; left: 0; right: 0; top: 212px;
    display: flex; align-items: center; justify-content: center; gap: 12px;
    font-family: "Arimo", Arial, sans-serif; font-size: 14px; letter-spacing: 2.5px;
  }
  .card-back .web .rule { width: 90px; height: 1px; background: rgba(255,255,255,.8); }

  /* Front: white */
  .card-front { left: 560px; top: 480px; background: var(--paper); color: var(--ink); }
  .card-front .logo-dot {
    position: absolute; left: 36px; top: 118px;
    width: 46px; height: 46px; border-radius: 50%; background: var(--teal);
  }
  .card-front .divider {
    position: absolute; left: 104px; top: 92px; width: 2px; height: 210px; background: var(--teal);
  }
  .card-front .brand-name {
    position: absolute; left: 116px; top: 90px;
    font-size: 21px; color: var(--logo-grey);
  }
  .details {
    position: absolute; left: 122px; top: 140px;
    font-family: "Arimo", Arial, sans-serif;
  }
  .details .name { color: var(--teal-dark); font-weight: 700; font-size: 18px; line-height: 22px; }
  .details .role { font-size: 14px; line-height: 19px; margin-bottom: 20px; }
  .details .contact { font-size: 14px; line-height: 19px; }
</style>
</head>
<body>
<main class="canvas">
  <section class="card card-back" aria-label="Business card back">
    <div class="brand">
      <span class="brand-dot"></span>
      <span class="brand-name">Bright Harbour Coaching</span>
    </div>
    <div class="web"><span class="rule"></span><span>www.bright-harbour.com</span><span class="rule"></span></div>
  </section>

  <section class="card card-front" aria-label="Business card front">
    <span class="logo-dot"></span>
    <span class="divider"></span>
    <span class="brand-name">Bright Harbour Coaching</span>
    <div class="details">
      <p class="name">Tamsin Varga</p>
      <p class="role">Personal Development<br>Coach &amp; Trainer</p>
      <p class="contact">+61 (0)452 819 407</p>
      <p class="contact">tamsin@bright-harbour.com</p>
      <p class="contact">www.bright-harbour.com</p>
    </div>
  </section>
</main>
</body>
</html>
```